Modern, pro female massage business needs business card design

We are a boutique, pro women's sports and remedial massage studio based in Singapore - we have a logo already (see attached image) and need to design a business card that reflects an elegant, modern and feminine feel using this logo.

We are focussed on a very local market and need to give a professional yet warm feeling.

Details for the card include (layout of your choice):

Talvina Brisk
Call, SMS or ChatBeam: 8317 6092
Email: tealmarrow@quenfold.com
Address: The Harbourview at Dunmore
82 Dunmore Road, East Coast, Singapore

To incorporate the OVAR logo (www.ovarglobe.co.uk) would be appreciated - see attached file.

Industry/Entity Type

Massage

Requirements
Nice to have
• We like the idea of using an embossed style card. Solid colour on the reverse - embossed on the front; four colour printing is okay.
Should not have
• It should not be uber 'girly girl' if that makes any sense. The logo is already colourful

```html
<!DOCTYPE html>
<html lang="en">
<head>
<meta charset="utf-8">
<title>Tealmarrow – Business Card</title>
<link href="https://fonts.googleapis.com/css2?family=Nunito:wght@800&family=PT+Sans:wght@400;700&display=swap" rel="stylesheet">
<style>
  :root {
    --backdrop: #3d4c4f;
    --pink-deep: #d81b7a;
    --pink-mid: #ee4f9a;
    --pink-light: #f6a8cc;
    --pink-band: #c4156c;
    --cream: #f3efe6;
    --leaf-green: #7db52f;
    --ink: #2e2a2c;
    --ink-soft: #4a4245;
    --flourish-pink: #d41672;
  }
  * { box-sizing: border-box; margin: 0; padding: 0; }
  html, body { width: 1200px; height: 1000px; overflow: hidden; }
  body {
    background: var(--backdrop);
    font-family: "PT Sans", Arial, sans-serif;
    position: relative;
  }
  .card {
    position: absolute;
    width: 520px;
    height: 300px;
    border-radius: 4px;
    overflow: hidden;
    box-shadow: 0 14px 30px rgba(0,0,0,.35);
  }
  /* Front card */
  .card--front {
    left: 60px; top: 350px;
    background: linear-gradient(115deg, var(--pink-deep) 0%, var(--pink-light) 45%, var(--pink-mid) 100%);
  }
  .side-band {
    position: absolute; right: 0; top: 0; bottom: 0; width: 40px;
    background: var(--pink-band);
    display: flex; align-items: center; justify-content: center;
  }
  .side-band__url {
    writing-mode: vertical-rl;
    color: #fbd3e6; font-size: 11px; letter-spacing: .5px;
  }
  .partner-badge {
    position: absolute; right: 56px; top: 18px;
    width: 40px; height: 40px; border-radius: 4px;
    background: #3a5d9c; border: 2px solid #fff;
  }
  .holder-name {
    position: absolute; right: 60px; top: 96px;
    color: var(--pink-deep); font-weight: 700; font-size: 30px;
  }
  .brand {
    position: absolute; left: 30px; top: 66px;
  }
  .brand__name {
    font-family: "Nunito", Arial, sans-serif; font-weight: 800;
    font-size: 44px; line-height: 1; color: var(--leaf-green); letter-spacing: -1px;
  }
  .brand__tagline {
    font-size: 14px; color: var(--ink-soft); margin-top: 2px; padding-left: 4px;
  }
  .flourish-front {
    position: absolute; left: 0; bottom: 0; width: 200px; height: 130px;
    background: radial-gradient(ellipse at 20% 100%, var(--flourish-pink) 0%, rgba(212,22,114,.5) 45%, rgba(212,22,114,0) 75%);
  }
  .contacts {
    position: absolute; left: 200px; bottom: 28px;
    list-style: none; color: var(--ink); font-size: 13px; font-weight: 700; line-height: 1.35;
  }
  .contacts li { display: flex; gap: 8px; align-items: flex-start; margin-top: 4px; }
  .contacts svg { width: 13px; height: 13px; flex: none; margin-top: 2px; fill: var(--ink); }
  /* Back card */
  .card--back {
    left: 620px; top: 350px;
    background: var(--cream);
  }
  .flourish-back {
    position: absolute; left: 0; top: 0; width: 220px; height: 110px;
    background: radial-gradient(ellipse at 25% 0%, var(--flourish-pink) 0%, rgba(212,22,114,.45) 45%, rgba(212,22,114,0) 75%);
  }
  .card--back .brand {
    left: 50%; top: 50%; transform: translate(-50%, -40%); text-align: left;
  }
  .card--back .brand__name { font-size: 60px; }
  .card--back .brand__tagline { font-size: 18px; }
</style>
</head>
<body>
  <section class="card card--front">
    <div class="flourish-front" role="img" aria-label="Pink floral flourish with tulip buds"></div>
    <div class="partner-badge" role="img" aria-label="Accreditation badge"></div>
    <div class="side-band"><span class="side-band__url">www.ovarglobe.co.uk</span></div>
    <div class="brand">
      <div class="brand__name">tealmarrow</div>
      <div class="brand__tagline">Remedial and sports massage</div>
    </div>
    <div class="holder-name">Talvina Brisk</div>
    <ul class="contacts">
      <li>
        <svg viewBox="0 0 16 16"><path d="M8 1 1 7h2v8h4v-5h2v5h4V7h2z"/></svg>
        <span>The Harbourview at Dunmore<br>82 Dunmore Road, East Coast, Singapore</span>
      </li>
      <li>
        <svg viewBox="0 0 16 16"><path d="M1 3h14v10H1z M2 4l6 5 6-5" fill="none" stroke="#2e2a2c" stroke-width="1.6"/></svg>
        <span>tealmarrow@quenfold.com</span>
      </li>
      <li>
        <svg viewBox="0 0 16 16"><path d="M4 1h3l1 4-2 1c1 2 2 3 4 4l1-2 4 1v3c0 1-1 2-2 2C7 14 2 9 2 3c0-1 1-2 2-2z"/></svg>
        <span>8317 6092 (Call, SMS or ChatBeam)</span>
      </li>
    </ul>
  </section>

  <section class="card card--back">
    <div class="flourish-back" role="img" aria-label="Pink floral flourish with tulip buds"></div>
    <div class="brand">
      <div class="brand__name">tealmarrow</div>
      <div class="brand__tagline">Remedial and sports massage</div>
    </div>
  </section>
</body>
</html>
```